Emergency Management Consulting Flyer

Company name: Stone Harbor Emergency Management

I am looking for a postcard design for my emergency management consulting business. I'm looking for something that has some colors and is double sided, on side with the information on services provided and the other side with the contact information. For the main side I'm looking for the following:

How prepared are you?

Services Provided:
Healthcare Preparedness
EOC Support
Emergency Planning
Mitigation Planning
Business Continuity
Disaster Response
Training and Exercises
Project Management
And more

Affordable for small and large organizations
Stand-by contracts available

On the back side, I'm looking for Contact Us section.

Overall I'm looking for something a bit more modern and need to have at least one disaster photo. If you have questions please message me.

Target Market(s)

Government, Healthcare Facilities, Businesses

Industry/Entity Type

Consulting

Requirements
Must have
• Disaster Picture, modern looking
• For the main side I'm looking for the following:
• How prepared are you?
• Services Provided:
• Healthcare Preparedness
• EOC Support
• Emergency Planning
• Mitigation Planning
• Business Continuity
• Disaster Response
• Training and Exercises
• Project Management
• And more
• Affordable for small and large organizations
• Stand-by contracts available

```html
<!DOCTYPE html>
<html lang="en">
<head>
<meta charset="utf-8">
<title>Stone Harbor Emergency Management – Services Postcard</title>
<link rel="stylesheet" href="https://fonts.googleapis.com/css2?family=Bebas+Neue&family=Open+Sans:wght@400;600;700;800&family=Roboto:wght@300;400&display=swap">
<style>
  :root {
    --orange: #ef6a23;
    --orange-deep: #e4541a;
    --ink: #3a3d42;
    --ink-soft: #4a4d52;
    --band: #262424;
    --white: #ffffff;
    --paper: #ffffff;
    --skin-light: #f3e4da;
    --skin-mid: #d9b6a3;
    --hair: #4b2f24;
  }
  * { box-sizing: border-box; margin: 0; padding: 0; }
  html, body { width: 1200px; height: 930px; overflow: hidden; background: var(--paper); }
  .postcard {
    position: relative;
    width: 1200px;
    height: 930px;
    overflow: hidden;
    background: var(--paper);
    font-family: "Roboto", Arial, sans-serif;
  }
  .hero-photo {
    position: absolute;
    left: 540px;
    top: 0;
    width: 660px;
    height: 790px;
    background:
      radial-gradient(ellipse 60% 45% at 62% 58%, var(--skin-light) 0%, var(--skin-mid) 55%, rgba(217,182,163,0) 100%),
      radial-gradient(ellipse 70% 40% at 70% 12%, var(--hair) 0%, rgba(75,47,36,0.55) 55%, rgba(75,47,36,0) 100%),
      linear-gradient(90deg, rgba(255,255,255,1) 0%, rgba(243,228,218,0.6) 30%, #e8d2c4 60%, #c9a28f 100%);
  }
  .brand {
    position: absolute;
    left: 48px;
    top: 58px;
    display: flex;
    align-items: center;
    gap: 18px;
  }
  .brand-mark {
    width: 96px;
    height: 96px;
    border-radius: 50%;
    background: var(--orange);
    flex: none;
  }
  .brand-name {
    font-family: "Open Sans", Arial, sans-serif;
    font-weight: 700;
    color: var(--ink);
    line-height: 1;
    text-transform: uppercase;
  }
  .brand-name .line-main { display: block; font-size: 52px; letter-spacing: 1px; }
  .brand-name .line-sub { display: block; font-size: 19px; letter-spacing: 6.5px; margin-top: 6px; }
  .services-title {
    position: absolute;
    left: 56px;
    top: 200px;
    font-family: "Open Sans", Arial, sans-serif;
    font-weight: 700;
    font-size: 47px;
    color: var(--ink-soft);
    letter-spacing: 0.5px;
  }
  .services-title .accent { color: var(--orange); }
  .service-bar {
    position: absolute;
    left: 56px;
    top: 270px;
    width: 46px;
    height: 428px;
    background: linear-gradient(180deg, var(--orange) 0%, var(--orange-deep) 100%);
  }
  .service-list {
    position: absolute;
    left: 56px;
    top: 270px;
    list-style: none;
  }
  .service-list li {
    display: flex;
    align-items: center;
    height: 53.5px;
    font-size: 27px;
    font-weight: 400;
    color: var(--ink-soft);
    text-transform: uppercase;
    letter-spacing: 0.3px;
  }
  .service-icon {
    width: 46px;
    height: 46px;
    display: flex;
    align-items: center;
    justify-content: center;
    margin-right: 22px;
    flex: none;
  }
  .service-icon svg { width: 24px; height: 24px; }
  .tagline-tab {
    position: absolute;
    left: 0;
    top: 740px;
    width: 690px;
    height: 52px;
    background: var(--orange);
    border-radius: 0 26px 0 0;
    color: var(--white);
    font-family: "Open Sans", Arial, sans-serif;
    font-weight: 700;
    font-size: 26px;
    line-height: 52px;
    padding-left: 52px;
  }
  .closing-band {
    position: absolute;
    left: 0;
    top: 790px;
    width: 1200px;
    height: 140px;
    background: var(--band);
  }
  .headline {
    position: absolute;
    left: 74px;
    top: 14px;
    font-family: "Bebas Neue", Impact, sans-serif;
    font-size: 112px;
    line-height: 1;
    color: var(--white);
    letter-spacing: 1px;
    white-space: nowrap;
  }
  .headline .accent { color: var(--orange); }
  .standby {
    position: absolute;
    left: 948px;
    top: 24px;
    font-family: "Roboto", Arial, sans-serif;
    font-weight: 400;
    font-size: 26px;
    line-height: 29px;
    color: var(--white);
    text-transform: uppercase;
    text-align: center;
    letter-spacing: 1.5px;
  }
  .standby .accent { color: var(--orange); font-weight: 700; font-family: "Open Sans", Arial, sans-serif; }
</style>
</head>
<body>
<main class="postcard">
  <div class="hero-photo" role="img" aria-label="Photo of a stressed woman holding her head in both hands"></div>

  <header class="brand">
    <span class="brand-mark"></span>
    <h1 class="brand-name">
      <span class="line-main">Stone Harbor</span>
      <span class="line-sub">Emergency Management</span>
    </h1>
  </header>

  <h2 class="services-title"><span class="accent">SERVICES</span> PROVIDED:</h2>

  <div class="service-bar"></div>
  <ul class="service-list">
    <li><span class="service-icon"><svg viewBox="0 0 24 24"><circle cx="12" cy="12" r="10" fill="none" stroke="#fff" stroke-width="2"/><path d="M12 7v10M7 12h10" stroke="#fff" stroke-width="2.5"/></svg></span>Healthcare Preparedness</li>
    <li><span class="service-icon"><svg viewBox="0 0 24 24"><path d="M12 3l7 3v5c0 5-3 8-7 10-4-2-7-5-7-10V6z" fill="none" stroke="#fff" stroke-width="1.8"/><path d="M9 12l2 2 4-4" fill="none" stroke="#fff" stroke-width="1.8"/></svg></span>EOC Support</li>
    <li><span class="service-icon"><svg viewBox="0 0 24 24"><path d="M12 3l10 18H2z" fill="none" stroke="#fff" stroke-width="1.8"/><path d="M12 9v6M12 17v2" stroke="#fff" stroke-width="2"/></svg></span>Emergency Planning</li>
    <li><span class="service-icon"><svg viewBox="0 0 24 24"><circle cx="12" cy="5" r="2.5" fill="#fff"/><path d="M12 8l-4 6h3l-2 7M12 8l3 5h-3l3 8" fill="none" stroke="#fff" stroke-width="2"/></svg></span>Mitigation Planning</li>
    <li><span class="service-icon"><svg viewBox="0 0 24 24"><rect x="3" y="8" width="18" height="12" rx="1.5" fill="none" stroke="#fff" stroke-width="1.8"/><path d="M9 8V5h6v3M3 13h18" fill="none" stroke="#fff" stroke-width="1.8"/></svg></span>Business Continuity</li>
    <li><span class="service-icon"><svg viewBox="0 0 24 24"><circle cx="12" cy="4.5" r="2.5" fill="#fff"/><path d="M12 8v7M8 10h8M12 15l-3 6M12 15l3 6" fill="none" stroke="#fff" stroke-width="2"/></svg></span>Disaster Response</li>
    <li><span class="service-icon"><svg viewBox="0 0 24 24"><circle cx="6" cy="5" r="2.3" fill="#fff"/><path d="M6 8v13M6 11l5-2" fill="none" stroke="#fff" stroke-width="2"/><rect x="12" y="4" width="10" height="8" fill="none" stroke="#fff" stroke-width="1.6"/></svg></span>Training and Exercises</li>
    <li><span class="service-icon"><svg viewBox="0 0 24 24"><circle cx="8" cy="8" r="3" fill="#fff"/><path d="M3 20c0-4 2-7 5-7s5 3 5 7z" fill="#fff"/><rect x="14" y="6" width="8" height="12" fill="none" stroke="#fff" stroke-width="1.6"/><path d="M16 10h4M16 13h4" stroke="#fff" stroke-width="1.4"/></svg></span>Project Management</li>
  </ul>

  <div class="tagline-tab">Affordable for small and large organizations</div>

  <footer class="closing-band">
    <p class="headline"><span class="accent">HOW PREPARED</span> ARE YOU?</p>
    <p class="standby">Stand-by<br><span class="accent">Contracts</span><br>Available</p>
  </footer>
</main>
</body>
</html>
```